New Company Business Card Design

I have a new company logo and I want a new business card design. I dont know if the logo file i attached is in the correct format or quality. We are a New York City Specialty construction Firm specializing in high risk out of the box projects. I want a simple and classy business card that people will his card is as crisp as the work his company does.

Target Market(s)

Clients in the heavy construction industry in New York City

Industry/Entity Type

Construction Company

Contact Information for Business Card

Simple Classy - DIFFERENT

Font styles to use
Other font styles liked:
• Mach the logo font in some way

Colors

Designer to choose colors to be used in the design.

Requirements
Must have
• Uniqueness
Nice to have
• Nothing particular - Just different and classy - Timeless
Should not have
• Goofy Shit or Gimmicky shit

```html
<!DOCTYPE html>
<html lang="en">
<head>
<meta charset="UTF-8">
<title>Korvan Builders, Inc. — Business Card</title>
<link href="https://fonts.googleapis.com/css2?family=Montserrat:wght@400;500;700;800&display=swap" rel="stylesheet">
<style>
  :root {
    --stage: #1c1d20;
    --card-dark: #111214;
    --card-light: #eef0f2;
    --brand-blue: #1f8fd8;
    --brand-blue-deep: #1565b0;
    --ink-white: #ffffff;
    --ink-soft: #d9dbe0;
    --crane-grey: #3a3c40;
  }
  * { box-sizing: border-box; margin: 0; padding: 0; }
  html, body {
    width: 1200px;
    height: 900px;
    overflow: hidden;
    background: var(--stage);
    font-family: "Montserrat", sans-serif;
  }
  .stage {
    width: 1200px;
    height: 900px;
    display: flex;
    align-items: center;
    justify-content: center;
    gap: 50px;
  }
  .card {
    width: 525px;
    height: 300px;
    position: relative;
    overflow: hidden;
    border-radius: 4px;
    box-shadow: 0 18px 40px rgba(0,0,0,0.55);
  }

  /* Back: contact side */
  .card--contact {
    background: var(--card-dark);
    color: var(--ink-white);
  }
  .card--contact .edge-band {
    position: absolute;
    left: 0; right: 0; bottom: 0;
    height: 18px;
    background: linear-gradient(90deg, var(--brand-blue-deep), var(--brand-blue));
  }
  .holder {
    position: absolute;
    left: 34px; top: 30px;
  }
  .holder__name {
    font-size: 21px;
    font-weight: 500;
    letter-spacing: 0.5px;
    color: var(--brand-blue);
  }
  .holder__name strong {
    font-weight: 700;
    color: var(--ink-white);
  }
  .holder__role {
    font-size: 12px;
    font-weight: 500;
    letter-spacing: 1px;
    margin-top: 4px;
    color: var(--ink-soft);
  }
  .contact-list {
    position: absolute;
    left: 34px; top: 102px;
    list-style: none;
    font-size: 12.5px;
    color: var(--ink-soft);
    line-height: 1.45;
  }
  .contact-list .address { margin-bottom: 12px; }
  .contact-list .line {
    display: flex;
    align-items: center;
    gap: 9px;
    margin-bottom: 8px;
  }
  .contact-list .icon {
    width: 17px; height: 17px;
    flex: none;
  }
  .accent { color: var(--brand-blue); }

  .crane-art {
    position: absolute;
    left: 215px; top: 70px;
    width: 170px; height: 212px;
    background: linear-gradient(180deg, #2a2c30, var(--crane-grey));
    border-radius: 2px;
    opacity: 0.85;
  }
  .wordmark--contact {
    position: absolute;
    right: 30px; top: 96px;
    text-align: right;
    font-weight: 800;
    color: var(--ink-white);
    font-size: 30px;
    letter-spacing: 1px;
    line-height: 1;
  }
  .wordmark--contact span {
    display: block;
    font-size: 11px;
    letter-spacing: 3px;
    margin-top: 6px;
    font-weight: 800;
  }
  .web {
    position: absolute;
    right: 30px; bottom: 38px;
    font-size: 28px;
    font-weight: 700;
    letter-spacing: 1px;
    color: var(--ink-white);
  }
  .web .accent { color: var(--brand-blue); }

  /* Front: logo side */
  .card--brand {
    background:
      radial-gradient(circle at 30% 25%, rgba(160,185,210,0.18), transparent 45%),
      radial-gradient(circle at 75% 80%, rgba(150,175,205,0.2), transparent 40%),
      var(--card-light);
    display: flex;
    align-items: center;
    justify-content: center;
  }
  .wordmark--brand {
    text-align: center;
    font-weight: 800;
    color: var(--brand-blue-deep);
    line-height: 1;
  }
  .wordmark--brand .wordmark__main {
    display: block;
    font-size: 72px;
    letter-spacing: 2px;
  }
  .wordmark--brand .wordmark__sub {
    display: block;
    font-size: 20px;
    letter-spacing: 7px;
    margin-top: 12px;
  }
</style>
</head>
<body>
<main class="stage">
  <section class="card card--contact" aria-label="Business card, contact side">
    <div class="crane-art" role="img" aria-label="Grey silhouette illustration of a lattice-boom crawler crane"></div>

    <div class="holder">
      <p class="holder__name">MARCUS <strong>ELLERY</strong></p>
      <p class="holder__role">OWNER</p>
    </div>

    <ul class="contact-list">
      <li class="address">48 Harbor Row<br>Linden, NJ 07036</li>
      <li class="line">
        <svg class="icon" viewBox="0 0 20 20" aria-hidden="true">
          <circle cx="10" cy="10" r="10" fill="var(--brand-blue)"/>
          <path d="M6.3 5.2c.4-.3 1-.2 1.3.2l1.1 1.7c.3.4.2 1-.2 1.3l-.7.5c.5 1.2 1.4 2.2 2.6 2.8l.5-.7c.3-.4.9-.5 1.3-.2l1.7 1.1c.4.3.5.9.2 1.3l-.6.9c-.4.6-1.2.8-1.9.5-2.9-1.2-5-3.4-6.1-6.3-.3-.7 0-1.5.5-1.9z" fill="#111214"/>
        </svg>
        (555) 214-0187
      </li>
      <li class="line">
        <svg class="icon" viewBox="0 0 20 20" aria-hidden="true">
          <circle cx="10" cy="10" r="10" fill="var(--brand-blue)"/>
          <rect x="5" y="6.5" width="10" height="7" rx="1" fill="#111214"/>
          <path d="M5.4 7l4.6 3.6L14.6 7" fill="none" stroke="var(--brand-blue)" stroke-width="1"/>
        </svg>
        hello@<span class="accent">KORVAN</span>.COM
      </li>
    </ul>

    <p class="wordmark--contact">KORVAN<span>BUILDERS, INC.</span></p>

    <p class="web"><span class="accent">KORVAN</span>.COM</p>

    <div class="edge-band"></div>
  </section>

  <section class="card card--brand" aria-label="Business card, logo side">
    <p class="wordmark--brand">
      <span class="wordmark__main">KORVAN</span>
      <span class="wordmark__sub">BUILDERS, INC.</span>
    </p>
  </section>
</main>
</body>
</html>
```